Label Design for Cold pressed oils

We need a label designed for our cold pressed oil products. Our brand is called 'Velmarise'. We have 2 cold pressed oils, coconut oil and groundnut oil. We are selling healthy premium product so we want our packaging to appeal to the health conscious demographic. Label is a big part of the overall packaging.

Target Market(s)

Natural Food Stores, Retail Stores.

Industry/Entity Type

Coconut oil

Font styles to use
Script

Colors

Designer to choose colors to be used in the design.

Requirements
Must have
• We are planning to have a label on round containers. Label size should be 180mm length X 100 mm width.
• The label must highlight 'Cold Pressed' and 'Wood Churned'. It also needs to have 3-4 keywords like Raw, Hexane free, Unbleached & Unrefined, No Adulteration, No Preservatives, Nutrient rich, Additive free. Other things include.
• 1. Logo of the brand, Velmarise. You can design it as per your liking.
• 2. Product Name: Coconut Oil / Ground nut Oil
• 3. Volume: 500ml / 1000 ml.
• 4. Manufactured By: Tarvendi Holdings Ltd. Orlith, Meravan. 000000
• 5. Placeholder to mention website and customer care number.
• 6. Area to mention Batch information like Net weight, Batch No, Packaging Date, MRP. It should also mention 'Best before 6 month from packing'
• 7. Area to mention Nutritional values.
• 8. FSSAI number. I have uploaded a logo for FSSAI.
• 9. Barcode
• 10. It should have a vegetarian symbol as well. I have uploaded the image for it.
• It needs to say Product of India.
Nice to have
• It should have following: All our cold pressed oils are made from locally sourced responsibly produced raw materials. We make our oils using traditional methods in Kelbor wood churner where the temperature never goes above 35'C. We use natural method for filtering without any adulteration.

```html
<!DOCTYPE html>
<html lang="en">
<head>
<meta charset="utf-8">
<title>Velmarise Coconut Oil Label</title>
<link href="https://fonts.googleapis.com/css2?family=Stint+Ultra+Condensed&family=Arimo:wght@400;700&display=swap" rel="stylesheet">
<style>
  :root {
    --leaf: #7aab3a;
    --leaf-dark: #3f7a22;
    --paper: #ffffff;
    --page: #ffffff;
  }
  * { margin: 0; padding: 0; box-sizing: border-box; }
  html, body { width: 1200px; height: 800px; overflow: hidden; background: var(--page); }
  .label {
    position: absolute; left: 100px; top: 120px; width: 1000px; height: 560px;
    background: var(--paper); font-family: "Arimo", Arial, sans-serif; color: var(--leaf);
  }
  .band { position: absolute; top: 0; height: 100%; background: var(--leaf); }
  .band--left { left: 0; width: 86px; }
  .band--right { left: 910px; width: 90px; }
  .cut-line { position: absolute; left: 0; top: 0; width: 1000px; height: 560px; }

  .ingredients { position: absolute; left: 156px; top: 76px; width: 205px; font-size: 12.5px; line-height: 14px; }
  .ingredients h3 { font-size: 12.5px; font-weight: 700; }
  .ingredients-rule { position: absolute; left: 146px; top: 201px; width: 260px; height: 11px; background: var(--leaf); }

  .nutrition { position: absolute; left: 180px; top: 219px; width: 196px; height: 170px; background: var(--leaf); color: #fff; padding: 6px 8px; font-size: 6.5px; line-height: 8px; }
  .nutrition h4 { font-size: 10px; font-weight: 700; line-height: 12px; border-bottom: 1px solid #fff; padding-bottom: 2px; margin-bottom: 3px; }
  .nutrition .row { display: flex; justify-content: space-between; }
  .nutrition .rule { border-top: 1px solid #fff; margin: 3px 0; }
  .nutrition .bold { font-weight: 700; }

  .best-before { position: absolute; left: 148px; top: 529px; transform: rotate(-90deg); transform-origin: 0 0; font-size: 9.5px; line-height: 11px; white-space: nowrap; }
  .fssai-badge { position: absolute; left: 172px; top: 405px; width: 62px; height: 36px; border: 2px solid var(--leaf); border-radius: 4px; }
  .fssai-number { position: absolute; left: 178px; top: 443px; font-size: 10px; line-height: 11px; }
  .contact { position: absolute; left: 168px; top: 465px; font-size: 11px; line-height: 12px; font-weight: 700; }
  .maker { position: absolute; left: 168px; top: 497px; font-size: 10.5px; line-height: 12.5px; }
  .maker b { display: block; }

  .batch-tag { position: absolute; left: 345px; top: 417px; width: 16px; height: 109px; background: var(--leaf); }
  .batch-tag span { position: absolute; left: 2px; top: 104px; transform: rotate(-90deg); transform-origin: 0 0; color: #fff; font-size: 9px; font-weight: 700; white-space: nowrap; line-height: 12px; }
  .batch-info { position: absolute; left: 368px; top: 526px; width: 110px; transform: rotate(-90deg); transform-origin: 0 0; font-size: 8px; line-height: 9.5px; white-space: nowrap; }
  .batch-info .row { display: flex; justify-content: space-between; }

  .veg-mark { position: absolute; left: 622px; top: 47px; width: 28px; height: 28px; border: 2px solid var(--leaf); }
  .veg-mark::after { content: ""; position: absolute; left: 5px; top: 5px; width: 14px; height: 14px; border-radius: 50%; background: var(--leaf); }
  .volume { position: absolute; left: 782px; top: 38px; font-family: "Stint Ultra Condensed", serif; font-size: 32px; line-height: 40px; }

  .brand { position: absolute; left: 612px; top: 140px; display: flex; align-items: center; gap: 8px; font-family: "Stint Ultra Condensed", serif; font-size: 54px; line-height: 60px; }
  .brand-dot { width: 14px; height: 14px; border-radius: 50%; background: var(--leaf); }

  .product-name { position: absolute; left: 612px; top: 255px; font-family: "Stint Ultra Condensed", serif; font-size: 58px; line-height: 60px; font-weight: 400; }
  .product-name span { display: block; }
  .product-name .indent { padding-left: 6px; }
  .claims { position: absolute; left: 599px; top: 474px; font-family: "Stint Ultra Condensed", serif; font-size: 22px; line-height: 28px; }
</style>
</head>
<body>
  <section class="label">
    <div class="band band--left"></div>
    <div class="band band--right"></div>
    <svg class="cut-line" viewBox="0 0 1000 560" aria-hidden="true">
      <rect x="12" y="13" width="974" height="543" fill="none" stroke="#3f7a22" stroke-width="1.5" stroke-dasharray="4 3"/>
    </svg>

    <div class="ingredients">
      <h3>INGREDIENTS:</h3>
      <p>Lorem Ipsum is simply dummy text of the printing and typesetting industry. Lorem Ipsum has been the industry's standard dummy text ever since the 1500s, when an unknown printer took a galley of type and scrambled it to make a type specimen book.</p>
    </div>
    <div class="ingredients-rule"></div>

    <div class="nutrition">
      <h4>Nutrition Facts</h4>
      <div>Serving Size 12g</div>
      <div>Serving per packet 2</div>
      <div class="rule"></div>
      <div class="bold">Amount Per Serving</div>
      <div class="rule"></div>
      <div class="row"><span>Calories&nbsp;&nbsp;&nbsp;&nbsp;54</span><span>Calories From Fat&nbsp;&nbsp;19</span></div>
      <div class="row"><span>Energy in Kj&nbsp;&nbsp;229</span><span>% Daily Value</span></div>
      <div class="rule"></div>
      <div class="row"><span>Total Fat&nbsp;&nbsp;2g</span><span>16.7%</span></div>
      <div class="row"><span>Saturated Fat&nbsp;&nbsp;0.1g</span><span>0.8%</span></div>
      <div class="row"><span>Cholesterol&nbsp;&nbsp;0g</span><span>0%</span></div>
      <div class="row"><span>Sodium&nbsp;&nbsp;0.02</span><span>0.0%</span></div>
      <div class="row"><span>Total Carbohydrates&nbsp;&nbsp;8g</span><span>97%</span></div>
      <div class="row"><span>Sugar&nbsp;&nbsp;2g</span><span>16.2%</span></div>
      <div class="row"><span>Protein&nbsp;&nbsp;0.6g</span><span>0%</span></div>
      <div class="rule"></div>
      <div class="row"><span>Vitamin A&nbsp;&nbsp;0%</span><span>Vitamin C&nbsp;&nbsp;0%</span></div>
      <div class="row"><span>Calcium&nbsp;&nbsp;0%</span><span>Iron&nbsp;&nbsp;0%</span></div>
    </div>

    <div class="best-before">Best before 6 month from packing</div>
    <div class="fssai-badge" role="img" aria-label="Food safety licence badge"></div>
    <div class="fssai-number">00 00 00 00 00</div>
    <div class="contact">www.velmarise.com<br>Customer Care: 000 111 000</div>
    <div class="maker"><b>Manufactured By:</b>Tarvendi Holdings Ltd. Orlith,<br>Meravan. 000000</div>

    <div class="batch-tag"><span>BATCH NUMBER</span></div>
    <div class="batch-info">
      <div class="row"><span>Net weight,</span><span>500 ml</span></div>
      <div class="row"><span>Batch No,</span><span>000234</span></div>
      <div class="row"><span>Packaging Date,</span><span>15-2019</span></div>
      <div class="row"><span>MRP</span><span>1000</span></div>
    </div>

    <div class="veg-mark" role="img" aria-label="Vegetarian symbol"></div>
    <div class="volume">500ml</div>

    <div class="brand"><span class="brand-dot"></span><span>Velmarise</span></div>

    <h1 class="product-name">
      <span>Cold Pressed &amp;</span>
      <span>Wood Churned</span>
      <span class="indent">Coconut Oil</span>
    </h1>
    <p class="claims">Hexane Free, Unbleached<br>&amp; Unrefined, Nutrient Rich</p>
  </section>
</body>
</html>
```